Design Letterhead and Business Card for a technical solutions company

Please refer to the attached document for the details to be included in the letterhead and business cards. Logo and contact details enclosed therein. Client is looking for a professional image.

Please include as many contact details as possible in your entries.

```html
<!DOCTYPE html>
<html lang="en">
<head>
<meta charset="utf-8">
<title>Vantoro Technical Solutions – Business Card</title>
<link href="https://fonts.googleapis.com/css2?family=Arimo:wght@400;700&display=swap" rel="stylesheet">
<style>
  :root {
    --page-bg: #e9ebee;
    --card-blue: #2f6fae;
    --card-blue-light: #4f93cf;
    --card-blue-dark: #1f5187;
    --panel-navy: #1d4d80;
    --panel-edge: #6f9dc9;
    --tab-pale: #8db5da;
    --ink-dark: #0d2340;
    --ink-light: #ffffff;
    --band-navy: #1a4277;
  }
  * { box-sizing: border-box; margin: 0; padding: 0; }
  html, body { width: 1200px; height: 809px; overflow: hidden; }
  body {
    background: var(--page-bg);
    font-family: "Arimo", Arial, sans-serif;
    display: flex;
    align-items: center;
    justify-content: center;
    gap: 60px;
  }
  .card {
    position: relative;
    width: 540px;
    height: 310px;
    border-radius: 4px;
    overflow: hidden;
    background: radial-gradient(ellipse at 50% 40%, var(--card-blue-light) 0%, var(--card-blue) 55%, var(--card-blue-dark) 100%);
    box-shadow: 0 10px 30px rgba(20, 40, 70, 0.25);
  }

  /* Contact side */
  .contact-tab {
    position: absolute;
    left: 120px; top: 30px;
    width: 300px; height: 230px;
    background: var(--tab-pale);
    border-radius: 10px;
  }
  .contact-tab__label {
    position: absolute;
    left: 0; right: 0; bottom: 12px;
    text-align: center;
    font-size: 16px;
    color: var(--ink-dark);
  }
  .contact-panel {
    position: absolute;
    left: 95px; top: 30px;
    width: 350px; height: 190px;
    background: var(--panel-navy);
    border: 2px solid var(--panel-edge);
    border-radius: 22px;
    padding: 22px 30px;
    color: var(--ink-dark);
  }
  .contact-panel__name {
    font-size: 20px;
    text-align: center;
    margin-bottom: 10px;
  }
  .contact-list { list-style: none; }
  .contact-list li {
    display: flex;
    align-items: flex-start;
    gap: 10px;
    font-size: 15px;
    line-height: 1.3;
    margin-bottom: 4px;
  }
  .contact-list svg { flex: none; width: 14px; height: 14px; margin-top: 2px; }

  /* Brand side */
  .brand-band {
    position: absolute;
    left: 30px; top: 200px;
    width: 420px; height: 56px;
    background: linear-gradient(90deg, var(--band-navy), var(--card-blue-dark));
    display: flex;
    align-items: center;
    padding-left: 24px;
    gap: 14px;
  }
  .brand-band__name {
    color: var(--ink-light);
    font-weight: 700;
    font-size: 22px;
    letter-spacing: 1px;
  }
  .brand-mark {
    position: absolute;
    left: 430px; top: 198px;
    width: 62px; height: 62px;
    border-radius: 50%;
    background: var(--card-blue-light);
  }
  .brand-glow {
    position: absolute;
    left: 60px; top: 20px;
    width: 220px; height: 160px;
    border-radius: 50%;
    background: radial-gradient(circle, rgba(120,180,230,0.25), rgba(120,180,230,0) 70%);
  }
</style>
</head>
<body>
  <section class="card card--contact">
    <div class="contact-tab"><span class="contact-tab__label">Contact</span></div>
    <div class="contact-panel">
      <p class="contact-panel__name">K.L.Mendes</p>
      <ul class="contact-list">
        <li>
          <svg viewBox="0 0 16 16" aria-hidden="true"><circle cx="8" cy="8" r="7" fill="none" stroke="#0d2340" stroke-width="1.4"/><path d="M5.5 4.5l1.3 1.3-.8 1.1a5 5 0 0 0 2.6 2.6l1.1-.8 1.3 1.3-.9 1.1A6 6 0 0 1 4.4 5.4z" fill="#0d2340"/></svg>
          +0123 555 0147
        </li>
        <li>
          <svg viewBox="0 0 16 16" aria-hidden="true"><circle cx="8" cy="8" r="7" fill="none" stroke="#0d2340" stroke-width="1.4"/><path d="M5.5 4.5l1.3 1.3-.8 1.1a5 5 0 0 0 2.6 2.6l1.1-.8 1.3 1.3-.9 1.1A6 6 0 0 1 4.4 5.4z" fill="#0d2340"/></svg>
          +2751 555 0192
        </li>
        <li>
          <svg viewBox="0 0 16 16" aria-hidden="true"><circle cx="8" cy="8" r="7" fill="none" stroke="#0d2340" stroke-width="1.4"/><circle cx="8" cy="8" r="2.2" fill="none" stroke="#0d2340" stroke-width="1.3"/><path d="M10.2 6v3a1.2 1.2 0 0 0 2.4 0V8" fill="none" stroke="#0d2340" stroke-width="1.3"/></svg>
          kl.mendes@vantoro.com
        </li>
        <li>
          <svg viewBox="0 0 16 16" aria-hidden="true"><path d="M8 1a5 5 0 0 0-5 5c0 4 5 9 5 9s5-5 5-9a5 5 0 0 0-5-5zm0 7a2 2 0 1 1 0-4 2 2 0 0 1 0 4z" fill="#0d2340"/></svg>
          22/B Harlow Lane, Eastfield,<br>Brookton-4410
        </li>
      </ul>
    </div>
  </section>

  <section class="card card--brand">
    <div class="brand-glow"></div>
    <div class="brand-band">
      <span class="brand-band__name">VANTORO TECHNICAL SOLUTIONS</span>
    </div>
    <div class="brand-mark"></div>
  </section>
</body>
</html>
```